Business Card Design

Velvet Pixel Promotions

An online marketing consulting & strategy business for the cosmetic niche

We specialise in Increasing Leads, Conversions & Content Marketing

I am looking for a very clean, BOLD business card that is simple & effective

Target Market(s)

cosmetic surgeons & cosmetic clinics

Industry/Entity Type

Marketing

Contact Information for Business Card

Darren Okoye
Online Marketing Strategist

Darren@VelvetPixelPromotions.example
0491 268 517

LinkedIn: in/darrenokoye

```html
<!DOCTYPE html>
<html lang="en">
<head>
<meta charset="utf-8">
<title>Velvet Pixel Promotions – Business Card Concepts</title>
<link rel="stylesheet" href="https://fonts.googleapis.com/css2?family=Mulish:wght@400;600;700&display=swap">
<style>
  :root {
    --board: #ebebeb;
    --card: #ffffff;
    --green: #a6cf38;
    --blue: #00aeef;
    --teal: #1cb5c8;
    --ink: #231f20;
    --grey: #6d6e71;
    --label: #333333;
  }
  * { box-sizing: border-box; margin: 0; padding: 0; }
  html, body { width: 1200px; height: 782px; overflow: hidden; }
  body {
    background: var(--board);
    font-family: "Mulish", Arial, sans-serif;
    position: relative;
  }
  .concept-label {
    position: absolute;
    font-size: 22px;
    color: var(--label);
  }
  .card {
    position: absolute;
    width: 532px;
    background: var(--card);
    box-shadow: 2px 4px 8px rgba(0,0,0,0.25);
    overflow: hidden;
  }
  .card--rounded { height: 320px; border-radius: 28px; }
  .card--square { height: 322px; }
  .card-art { position: absolute; inset: 0; width: 100%; height: 100%; }

  .wordmark {
    position: absolute;
    display: flex;
    align-items: center;
    gap: 14px;
  }
  .wordmark-dot {
    border-radius: 50%;
    background: var(--teal);
    flex: none;
  }
  .wordmark-name {
    color: var(--grey);
    font-weight: 600;
    text-transform: uppercase;
    line-height: 1;
  }
  .wordmark-name span { display: block; }
  .wordmark--large .wordmark-dot { width: 72px; height: 72px; }
  .wordmark--large .wordmark-name { font-size: 37px; letter-spacing: 3px; }
  .wordmark--large .wordmark-name span + span { margin-top: 4px; }
  .wordmark--small .wordmark-dot { width: 40px; height: 40px; }
  .wordmark--small .wordmark-name { font-size: 18px; letter-spacing: 1.5px; gap: 8px; }
  .wordmark--small .wordmark-name span + span { margin-top: 2px; }

  .person { position: absolute; color: var(--ink); }
  .person-name { font-weight: 700; }
  .person-role { font-weight: 400; margin-top: 6px; }
  .contact-list { position: absolute; list-style: none; color: var(--ink); }
  .contact-list li { display: flex; align-items: center; gap: 7px; }
  .contact-icon { width: 16px; height: 16px; flex: none; }
  .profile-square { width: 16px; height: 16px; background: #0e76a8; border-radius: 2px; flex: none; }

  .card--rounded .person-name, .card--rounded .person-role { font-size: 15px; }
  .card--rounded .contact-list li { font-size: 15.5px; height: 24px; }
  .card--square .person-name { font-size: 16.5px; }
  .card--square .person-role { font-size: 16.5px; margin-top: 8px; }
  .card--square .contact-list li { font-size: 17px; height: 27px; }
</style>
</head>
<body>

  <span class="concept-label" style="left:20px; top:52px;">1</span>
  <span class="concept-label" style="left:28px; top:425px;">2</span>

  <!-- Concept 1: front -->
  <section class="card card--rounded" style="left:46px; top:43px;">
    <svg class="card-art" viewBox="0 0 532 320" preserveAspectRatio="none" aria-hidden="true">
      <path d="M0 0 L515 0 C350 5 150 40 0 105 Z" fill="var(--green)"/>
      <path d="M532 218 C400 272 200 308 25 320 L532 320 Z" fill="var(--blue)"/>
    </svg>
    <div class="wordmark wordmark--large" style="left:78px; top:112px;">
      <span class="wordmark-dot"></span>
      <p class="wordmark-name"><span>Velvet</span><span>Pixel</span><span>Promotions</span></p>
    </div>
  </section>

  <!-- Concept 1: back -->
  <section class="card card--rounded" style="left:623px; top:40px;">
    <svg class="card-art" viewBox="0 0 532 320" preserveAspectRatio="none" aria-hidden="true">
      <path d="M30 0 C200 8 400 40 532 102 L532 0 Z" fill="var(--green)"/>
      <path d="M0 218 C120 262 350 300 515 320 L0 320 Z" fill="var(--blue)"/>
    </svg>
    <div class="wordmark wordmark--small" style="left:36px; top:36px;">
      <span class="wordmark-dot"></span>
      <p class="wordmark-name"><span>Velvet</span><span>Pixel</span><span>Promotions</span></p>
    </div>
    <div class="person" style="left:111px; top:134px;">
      <p class="person-name">Darren Okoye</p>
      <p class="person-role">Online Marketing Strategist</p>
    </div>
    <ul class="contact-list" style="left:165px; top:184px;">
      <li>
        <svg class="contact-icon" viewBox="0 0 16 16" aria-hidden="true"><rect x="1" y="3" width="14" height="10" rx="1" fill="var(--blue)"/><path d="M1.5 4 L8 9 L14.5 4" fill="none" stroke="#fff" stroke-width="1.3"/></svg>
        Darren@VelvetPixelPromotions.example
      </li>
      <li>
        <svg class="contact-icon" viewBox="0 0 16 16" aria-hidden="true"><rect x="4" y="1" width="8" height="14" rx="1.5" fill="none" stroke="var(--blue)" stroke-width="1.5"/><circle cx="8" cy="12.3" r="0.9" fill="var(--blue)"/></svg>
        0491 268 517
      </li>
      <li><span class="profile-square"></span>in/darrenokoye</li>
    </ul>
  </section>

  <!-- Concept 2: front -->
  <section class="card card--square" style="left:53px; top:408px;">
    <svg class="card-art" viewBox="0 0 532 322" preserveAspectRatio="none" aria-hidden="true">
      <polygon points="0,2 532,2 532,36 300,36 278,18 0,18" fill="var(--green)"/>
      <polygon points="0,23 268,23 286,36 0,36" fill="var(--blue)"/>
      <polygon points="0,290 232,290 252,304 532,304 532,322 0,322" fill="var(--blue)"/>
      <polygon points="258,292 532,292 532,301 270,301" fill="var(--green)"/>
    </svg>
    <div class="wordmark wordmark--large" style="left:80px; top:112px;">
      <span class="wordmark-dot"></span>
      <p class="wordmark-name"><span>Velvet</span><span>Pixel</span><span>Promotions</span></p>
    </div>
  </section>

  <!-- Concept 2: back -->
  <section class="card card--square" style="left:632px; top:408px;">
    <svg class="card-art" viewBox="0 0 532 322" preserveAspectRatio="none" aria-hidden="true">
      <polygon points="0,2 532,2 532,36 300,36 278,18 0,18" fill="var(--green)"/>
      <polygon points="0,23 268,23 286,36 0,36" fill="var(--blue)"/>
      <polygon points="0,290 232,290 252,304 532,304 532,322 0,322" fill="var(--blue)"/>
      <polygon points="258,292 532,292 532,301 270,301" fill="var(--green)"/>
    </svg>
    <div class="person" style="left:59px; top:86px;">
      <p class="person-name">Darren Okoye</p>
      <p class="person-role">Online Marketing Strategist</p>
    </div>
    <ul class="contact-list" style="left:128px; top:168px;">
      <li>
        <svg class="contact-icon" viewBox="0 0 16 16" aria-hidden="true"><rect x="1" y="3" width="14" height="10" rx="1" fill="var(--blue)"/><path d="M1.5 4 L8 9 L14.5 4" fill="none" stroke="#fff" stroke-width="1.3"/></svg>
        Darren@VelvetPixelPromotions.example
      </li>
      <li>
        <svg class="contact-icon" viewBox="0 0 16 16" aria-hidden="true"><rect x="4" y="1" width="8" height="14" rx="1.5" fill="none" stroke="var(--blue)" stroke-width="1.5"/><circle cx="8" cy="12.3" r="0.9" fill="var(--blue)"/></svg>
        0491 268 517
      </li>
      <li><span class="profile-square"></span>in/darrenokoye</li>
    </ul>
  </section>

</body>
</html>
```